KORBALT

The business want a professional looking business card. We have a scetch we will add but want the extra upgrade, and would like more suggestions for variations of our business cards.

```html
<!DOCTYPE html>
<html lang="en">
<head>
<meta charset="utf-8">
<title>KORBALT Business Card</title>
<link rel="stylesheet" href="https://fonts.googleapis.com/css2?family=Cormorant+Garamond:wght@600;700&family=Source+Sans+3:wght@400&display=swap">
<style>
  :root {
    --backdrop: #bdbdbf;
    --ink-brown: #6a4f24;
    --card-brown: #644822;
    --gold: #e2c274;
    --grad-ivory: #ece9e1;
    --grad-cream: #f0e2b8;
    --grad-gold: #f6d98f;
    --grad-tan: #b39a64;
    --grad-dark: #6e552a;
    --grad-deep: #5f4620;
  }
  * { margin: 0; padding: 0; box-sizing: border-box; }
  html, body { width: 1200px; height: 960px; overflow: hidden; background: var(--backdrop); }
  .canvas { position: relative; width: 1200px; height: 960px; background: var(--backdrop); }

  .card { position: absolute; width: 724px; height: 414px; }
  .card-front {
    left: 166px; top: 62px;
    background: linear-gradient(90deg, var(--grad-ivory) 0%, var(--grad-cream) 22%, var(--grad-gold) 36%, var(--grad-tan) 52%, var(--grad-dark) 78%, var(--grad-deep) 100%);
  }
  .card-back { left: 277px; top: 502px; background: var(--card-brown); }

  .company-title {
    position: absolute; left: 49px; top: 45px;
    font-family: "Cormorant Garamond", serif; font-weight: 700;
    font-size: 31px; letter-spacing: 1px; color: var(--ink-brown); white-space: nowrap;
  }
  .role-block {
    position: absolute; left: 49px; top: 93px;
    font-family: "Source Sans 3", sans-serif; font-size: 17.5px; line-height: 27px;
    color: var(--ink-brown); text-transform: uppercase;
  }
  .contact-list { position: absolute; left: 44px; top: 308px; list-style: none; }
  .contact-list li {
    display: flex; align-items: center; height: 24px;
    font-family: "Source Sans 3", sans-serif; font-size: 19px; color: var(--ink-brown);
  }
  .contact-list svg { width: 17px; height: 17px; margin-right: 17px; flex: none; }

  .brand { position: absolute; display: flex; flex-direction: column; align-items: center; }
  .brand-dot { border-radius: 50%; background: var(--gold); }
  .brand-name {
    font-family: "Cormorant Garamond", serif; font-weight: 700;
    color: var(--gold); letter-spacing: 2px; white-space: nowrap;
  }
  .brand-front { left: 470px; top: 228px; width: 200px; }
  .brand-front .brand-dot { width: 44px; height: 44px; margin-bottom: 20px; }
  .brand-front .brand-name { font-size: 36px; line-height: 1; }
  .brand-back { left: 162px; top: 130px; width: 400px; }
  .brand-back .brand-dot { width: 72px; height: 72px; margin-bottom: 44px; }
  .brand-back .brand-name { font-size: 58px; line-height: 1; }
</style>
</head>
<body>
<div class="canvas">
  <section class="card card-front">
    <h1 class="company-title">KORBALT&nbsp; VANTHORNE</h1>
    <p class="role-block">CEO &amp; Founder<br>Aksel Rune Vanthorne</p>

    <ul class="contact-list">
      <li>
        <svg viewBox="0 0 24 24" aria-hidden="true"><path fill="#6a4f24" d="M6.6 10.8a15 15 0 0 0 6.6 6.6l2.2-2.2c.3-.3.7-.4 1-.2 1.1.4 2.3.6 3.6.6.6 0 1 .4 1 1V20c0 .6-.4 1-1 1A17 17 0 0 1 3 4c0-.6.4-1 1-1h3.5c.6 0 1 .4 1 1 0 1.3.2 2.5.6 3.6.1.3 0 .7-.2 1z"/></svg>
        004791234567
      </li>
      <li>
        <svg viewBox="0 0 24 24" aria-hidden="true"><path fill="#6a4f24" d="M2 8l10-6 10 6v13H2z"/><path fill="#f3e6c4" d="M4 9l8 5 8-5" stroke="#f3e6c4" stroke-width="1.5"/></svg>
        korbalt.llc@mailbox.com
      </li>
      <li>
        <svg viewBox="0 0 24 24" aria-hidden="true"><circle cx="12" cy="12" r="10" fill="#6a4f24"/><path d="M2 12h20M12 2c3 3 3 17 0 20M12 2c-3 3-3 17 0 20" stroke="#f0e2b8" stroke-width="1.2" fill="none"/></svg>
        www.korbalt.llc
      </li>
    </ul>

    <div class="brand brand-front">
      <span class="brand-dot"></span>
      <span class="brand-name">KORBALT</span>
    </div>
  </section>

  <section class="card card-back">
    <div class="brand brand-back">
      <span class="brand-dot"></span>
      <span class="brand-name">KORBALT</span>
    </div>
  </section>
</div>
</body>
</html>
```